Hypnotherapy- past life regression-life between lives therapist needs a website

I need a website that is enticing and spiritual in its feeling. It needs to have a lot of beautiful nature pictures included. The theme is "Quiet Harbor Path- what might you find....Lessons Solutions Answers"
Because all of us have the answers to living our best life, they are in our subconcious. But not everyone is capable of accessing them. Hypnosis accesses the subconcious and helps to create new neural pathways in the brain which can create new behaviors and responses to situations.
Hypnosis can help with anxiety, pain relief, weight loss, smoking/vaping cessation, self confidence......anything about yourself that you want to change.
Exploration of past lives and life between lives can reveal things related to ones current life. For example, perhaps your fear of deep water is a result of drowning in a past life. Once this has been discovered, it can lead to changes in ones current life.
Almost any personal behavior one wants to change, can be helped through hypnotherapy.
I need a page for testimonials, a place for scheduling (I will have a link to my scheduling app) some information about hypnotherapy.
I am uploading my logo files. My business card will be using the black and gold style, but my website does not have to reflect that. It can be based on the caramel and deep green like full color logo. Earthy, calm colors.
I also like the mock up of my logo on the beach and there was one on a starry night sky that I also liked.
Target Market(s)
men and women ages 25-50
Industry/Entity Type
natural health and wellness, spirituality
Number of Pages Required
4 page
Requirements
Must have
- a page for testimonials, perhaps with a beautiful nature picture with each one, I will have approximately 6. A link to schedule a complimentary intro session, preferably on the first page
Should not have
- no swinging watches or other sterotyped hypnosis symbols

```html
<!DOCTYPE html>
<html lang="en">
<head>
<meta charset="utf-8">
<title>Quiet Harbor Path – A Journey Within</title>
<link href="https://fonts.googleapis.com/css2?family=Libre+Baskerville:wght@400;700&family=Inter:wght@400;500;600;700&display=swap" rel="stylesheet">
<style>
:root{
  --olive:#5e5d2b;
  --olive-dark:#4b4a1f;
  --forest:#3e4c38;
  --forest-card:#435240;
  --caramel:#d8812c;
  --cream:#fbf1e6;
  --ink:#3b3b3b;
  --muted:#555;
  --footer:#3f4a3e;
  --footer-base:#323c31;
  --white:#fff;
}
*{margin:0;padding:0;box-sizing:border-box}
html,body{width:1200px;height:3730px;overflow:hidden;background:var(--white)}
body{position:relative;font-family:"Inter",sans-serif;color:var(--ink)}
.serif{font-family:"Libre Baskerville",serif}
.abs{position:absolute}

/* nav */
.brand{position:absolute;display:flex;align-items:center;gap:12px}
.brand-dot{width:40px;height:40px;border-radius:50%;border:2px solid var(--caramel)}
.brand-name{font-family:"Libre Baskerville",serif;font-size:19px;color:var(--caramel);letter-spacing:1px}
.nav-link{position:absolute;top:30px;font-size:12px;font-weight:600;letter-spacing:2px;color:#444}
.btn{position:absolute;display:flex;align-items:center;justify-content:center;border-radius:30px;font-size:12px;font-weight:700;letter-spacing:2px;text-transform:uppercase}
.btn-outline{border:2px solid var(--olive);color:var(--olive);background:var(--white)}
.btn-solid{background:var(--olive);color:var(--white)}
.btn-white{background:var(--white);color:var(--olive)}

/* hero */
.hero-kicker{left:84px;top:248px;font-size:22px;color:var(--caramel)}
.hero-title{left:84px;top:272px;font-size:62px;color:var(--olive-dark);letter-spacing:-1px}
.hero-text{left:84px;top:360px;width:520px;font-size:17.5px;line-height:26px;color:#3d3d3d}
.arch-frame{left:696px;top:123px;width:408px;height:565px;border:3px solid #c9c9c9;border-radius:204px 204px 0 0}
.arch-photo{left:704px;top:131px;width:392px;height:549px;border-radius:196px 196px 0 0;background:linear-gradient(180deg,#1e1a14 0%,#2f3a1c 30%,#4d6a2a 50%,#7a5136 72%,#8d8e8c 88%,#5d5e5c 100%)}

/* approach band */
.forest-photo{left:0;top:786px;width:1200px;height:728px;background:linear-gradient(90deg,#1f2715 0%,#3d4a22 30%,#a79f55 45%,#4e5a2b 60%,#2a321c 100%)}
.approach-card{left:634px;top:897px;width:466px;height:467px;background:rgba(62,76,56,.93);border-radius:26px}
.approach-title{left:686px;top:948px;font-size:41px;line-height:44px;color:var(--white)}
.label{font-size:14.5px;font-weight:700;letter-spacing:2.5px;color:var(--caramel);text-transform:uppercase}
.approach-text{left:687px;top:1092px;width:370px;font-size:13.5px;line-height:20.5px;color:#eef0ea}

/* services */
.section-title{font-size:57px;color:var(--olive-dark)}
.rule{position:absolute;height:1px;background:var(--caramel)}
.card{position:absolute;width:283px;height:350px;background:var(--white);border-radius:10px;box-shadow:0 6px 22px rgba(0,0,0,.07);text-align:center;padding:38px 22px 0}
.card-icon{width:88px;height:88px;margin:0 auto;border-radius:50%;background:#ecebe3}
.card-title{font-family:"Libre Baskerville",serif;font-size:18px;color:var(--olive);margin-top:26px;line-height:20px}
.card-text{font-size:13px;line-height:20.5px;color:#505050;margin-top:18px}
.card-more{position:absolute;left:785px;top:2181px;width:283px;height:351px;border-radius:10px;background:#4a6242;overflow:hidden}
.card-more-text{position:absolute;left:38px;top:170px;font-family:"Libre Baskerville",serif;font-size:34px;line-height:37px;color:var(--white)}

/* testimonials */
.testi-photo{left:84px;top:2820px;width:456px;height:482px;border-radius:30px;background:radial-gradient(circle at 65% 20%,#b7c489 0%,#5b7a2c 35%,#2c4619 70%,#14220c 100%)}
.quote-mark{position:absolute;top:2820px;width:126px;height:190px;background:var(--cream);border-radius:26px 26px 6px 60px}
.testi-name{left:630px;top:2904px;font-size:21px;color:#333}
.testi-text{left:630px;top:2986px;width:440px;font-size:17.5px;line-height:26px;color:#404040}
.counter{left:630px;top:3210px;font-size:40px;color:#444}
.counter small{font-size:20px;color:#999}

/* footer */
.footer{left:0;top:3428px;width:1200px;height:234px;background:var(--footer)}
.footer-base{left:0;top:3662px;width:1200px;height:68px;background:var(--footer-base);color:#e4e4e4;font-size:11.5px;text-align:center;line-height:68px}
.footer-head{font-family:"Libre Baskerville",serif;font-size:15px;color:#eaeaea}
.footer-link{font-size:11.5px;color:#eaeaea}
.footer-blurb{left:84px;top:3533px;width:300px;font-size:13px;line-height:20.5px;color:#eaeaea}
.social{position:absolute;top:3504px;width:20px;height:20px;border-radius:50%;border:1.6px solid #eaeaea}
</style>
</head>
<body>

<!-- navigation -->
<div class="brand" style="left:80px;top:16px">
  <span class="brand-dot"></span><span class="brand-name">QUIET HARBOR PATH</span>
</div>
<span class="nav-link" style="left:619px">HOME</span>
<span class="nav-link" style="left:692px">SERVICES</span>
<span class="nav-link" style="left:795px">TESTIMONIALS</span>
<a class="btn btn-outline" style="left:934px;top:17px;width:178px;height:39px">Schedule a call</a>

<!-- hero -->
<div class="abs serif hero-kicker">Quiet Harbor Path</div>
<h1 class="abs serif hero-title" style="font-weight:400">A Journey within.</h1>
<p class="abs hero-text">Unlock the power within you through the art of hypnotherapy. My serene approach blends the tranquility of nature with the profound exploration of your subconscious mind.</p>
<a class="btn btn-solid" style="left:84px;top:485px;width:196px;height:48px">Schedule a call</a>
<a class="btn btn-outline" style="left:295px;top:485px;width:158px;height:48px">Learn more</a>
<div class="abs arch-frame"></div>
<div class="abs arch-photo" role="img" aria-label="Arched stone doorway opening onto a lush tropical courtyard garden"></div>

<!-- approach -->
<div class="abs forest-photo" role="img" aria-label="Sunlit pine forest with a path through the trees"></div>
<div class="abs approach-card"></div>
<h2 class="abs serif approach-title" style="font-weight:400">Let’s Begin Your<br>Journey</h2>
<div class="rule" style="left:890px;top:1058px;width:48px"></div>
<div class="abs label" style="left:687px;top:1050px">My Approach</div>
<p class="abs approach-text">Our approach combines the ancient wisdom of hypnotherapy with a modern understanding of neuroscience. By accessing the subconscious, we pave the way for new neural pathways, fostering positive behaviors and responses to life’s challenges.</p>
<a class="btn btn-white" style="left:686px;top:1243px;width:196px;height:48px">Schedule a call</a>

<!-- services -->
<h2 class="abs serif section-title" style="left:0;width:1200px;text-align:center;top:1624px;font-weight:400">How Can I Help you</h2>
<div class="rule" style="left:415px;top:1722px;width:110px"></div>
<div class="rule" style="left:673px;top:1722px;width:112px"></div>
<div class="abs label" style="left:0;width:1200px;text-align:center;top:1713px">My Services</div>

<div class="card" style="left:124px;top:1780px">
  <div class="card-icon" role="img" aria-label="Line icon for anxiety relief"></div>
  <div class="card-title">Anxiety Relief Sessions:</div>
  <p class="card-text">My approach blends relaxation techniques and subconscious exploration to address the root causes of anxiety, paving the way for a calmer and more centered you.</p>
</div>
<div class="card" style="left:458px;top:1780px">
  <div class="card-icon" role="img" aria-label="Line icon for meditation and pain relief"></div>
  <div class="card-title">Pain Relief Solutions</div>
  <p class="card-text">My sessions focus on understanding the mind-body connection, helping you manage and alleviate pain by reshaping your perception and response to it.</p>
</div>
<div class="card" style="left:792px;top:1780px">
  <div class="card-icon" role="img" aria-label="Line icon of a scale for weight loss"></div>
  <div class="card-title">Weight Loss</div>
  <p class="card-text">My hypnotherapy sessions help you uncover and address the emotional and psychological aspects of weight management, fostering a positive relationship with your body.</p>
</div>
<div class="card" style="left:124px;top:2181px">
  <div class="card-icon" role="img" aria-label="Line icon of open hands for self-confidence"></div>
  <div class="card-title">Enhancing Self-Confidence:</div>
  <p class="card-text">Whether overcoming performance anxiety or boosting self-esteem, our approach focuses on building positive thought patterns, empowering you to navigate life with confidence.</p>
</div>
<div class="card" style="left:458px;top:2181px">
  <div class="card-icon" role="img" aria-label="Line icon of a radiant star for past life exploration"></div>
  <div class="card-title">Exploration of Past Lives<br>and Life Between Lives</div>
  <p class="card-text">Gain insights into current challenges, fears, and patterns by uncovering the wisdom embedded in your past. This transformative experience can lead to profound changes in your present life.</p>
</div>
<div class="card-more">
  <div class="card-more-text">Find out<br>more<br>services<br>I offer</div>
  <svg class="abs" style="left:200px;top:290px" width="42" height="20" viewBox="0 0 42 20"><path d="M2 10h36M30 3l8 7-8 7" fill="none" stroke="#fff" stroke-width="1.8"/></svg>
</div>

<!-- testimonials -->
<h2 class="abs serif" style="left:84px;top:2706px;font-size:42px;font-weight:400;color:#3a3a3a">Testimonials</h2>
<div class="rule" style="left:84px;top:2775px;width:72px"></div>
<div class="abs label" style="left:171px;top:2766px">From My Clients</div>
<div class="abs testi-photo" role="img" aria-label="Misty green rainforest canopy"></div>
<div class="quote-mark" style="left:793px"></div>
<div class="quote-mark" style="left:961px"></div>
<div class="abs serif testi-name">Marisol T</div>
<p class="abs testi-text">My journey with ‘Quiet Harbor Path’ has been nothing short of miraculous. Struggling with anxiety, I found solace through hypnotherapy. The serene atmosphere and expert guidance helped me unearth inner peace. Grateful for the transformative experience!</p>
<div class="abs serif counter">01<small>/06</small></div>
<svg class="abs" style="left:735px;top:3226px" width="42" height="20" viewBox="0 0 42 20"><path d="M40 10H4M12 3l-8 7 8 7" fill="none" stroke="#888" stroke-width="1.8"/></svg>
<svg class="abs" style="left:797px;top:3226px" width="42" height="20" viewBox="0 0 42 20"><path d="M2 10h36M30 3l8 7-8 7" fill="none" stroke="#333" stroke-width="1.8"/></svg>

<!-- footer -->
<div class="abs footer"></div>
<div class="brand" style="left:80px;top:3462px">
  <span class="brand-dot" style="border-color:#eaeaea"></span><span class="brand-name" style="color:#eaeaea">QUIET HARBOR PATH</span>
</div>
<p class="abs footer-blurb">“Quiet Harbor Path - A Journey Within.” Immerse yourself in the beauty of nature as we explore the depths of your subconscious to uncover Lessons, Solutions, and Answers.</p>
<div class="abs footer-head" style="left:540px;top:3468px">Sitemap</div>
<div class="abs footer-link" style="left:540px;top:3503px">Home</div>
<div class="abs footer-link" style="left:540px;top:3525px">Services</div>
<div class="abs footer-link" style="left:540px;top:3547px">Testimonials</div>
<div class="abs footer-head" style="left:873px;top:3468px">Connect</div>
<span class="social" style="left:873px" role="img" aria-label="Social profile"></span>
<span class="social" style="left:922px" role="img" aria-label="Social profile"></span>
<span class="social" style="left:970px" role="img" aria-label="Social profile"></span>
<svg class="abs" style="left:1018px;top:3505px" width="22" height="17" viewBox="0 0 22 17" role="img" aria-label="Email"><rect x="1" y="1" width="20" height="15" rx="2" fill="none" stroke="#eaeaea" stroke-width="1.6"/><path d="M1.5 2l9.5 7 9.5-7" fill="none" stroke="#eaeaea" stroke-width="1.6"/></svg>
<div class="abs footer-base">© 2023 WalkQuietHarborPath. All rights reserved.</div>

</body>
</html>
```